out of the box Business Card Design for a Manufacturer / Distributor

We are a manufarturer and distributor of products.
the company name is VORTANI (Pic attached)

the picture is NOT a must have on the business Card.

the Business Card should look really professional and/or special, so out of the box thinking is welcome.

there should be 2 Adresses on the Business Card for Main and Branch Office.
Email Adress, homepage, Name is required
NO Phone Number

Our working field:
Private Labeling
high Quality Production
direct distribution
warehousing
trademark registration
legal support

Main Office:
Kornblumenweg 14
08352 Lindenfeld
Germany

Branch Office:
Daska Lane
Zarinkot
Pakistan

Names:
Lukas Feldhaus (Owner)
Imran Qureshi (Owner)

Email:
lukas@vortani-example.com
imran@vortani-example.com

homepage:
vortani-example.com

Industry/Entity Type

Manufacturer Distributer

Contact Information for Business Card

Vortani

Requirements
Must have
• Names, both office Adresses, email, homepage
Should not have
• Phone Number

```html
<!DOCTYPE html>
<html lang="en">
<head>
<meta charset="utf-8">
<title>Vortani – Business Card</title>
<link href="https://fonts.googleapis.com/css2?family=Crimson+Pro:wght@400;600&family=Open+Sans:wght@400&display=swap" rel="stylesheet">
<style>
  :root {
    --page-bg: #c9c9c9;
    --card: #505050;
    --card-strip: #444444;
    --card-band: #2f2f2f;
    --ink: #ffffff;
    --ink-soft: #e6e6e6;
    --mark-soft: #8f8b8b;
  }
  * { box-sizing: border-box; margin: 0; padding: 0; }
  html, body {
    width: 1200px; height: 849px; overflow: hidden;
    background: var(--page-bg);
    font-family: "Crimson Pro", Georgia, serif;
  }
  .sheet { position: relative; width: 1200px; height: 849px; }

  .card {
    position: absolute;
    width: 440px; height: 252px;
    background: var(--card);
    color: var(--ink);
    overflow: hidden;
  }

  /* Back side */
  .card--back { left: 110px; top: 190px; }
  .card--back .back-mark {
    position: absolute; left: 48px; top: 62px;
    width: 110px; height: 110px; border-radius: 50%;
    background: var(--mark-soft);
  }
  .offices {
    position: absolute; left: 200px; top: 50px;
    font-size: 15px; line-height: 1.15; color: var(--ink-soft);
  }
  .office + .office { margin-top: 16px; }
  .office__title { font-weight: 600; color: var(--ink); letter-spacing: 0.02em; }

  /* Front side */
  .card--front { left: 650px; top: 190px; }
  .brand {
    position: absolute; left: 34px; top: 50px;
    display: flex; align-items: center; gap: 16px;
  }
  .brand__dot { width: 64px; height: 64px; border-radius: 50%; background: var(--ink); }
  .brand__name { font-size: 40px; font-weight: 400; letter-spacing: 0.06em; color: var(--ink); }
  .person {
    position: absolute; left: 114px; top: 122px;
    font-size: 15px; line-height: 1.2;
  }
  .person__name { letter-spacing: 0.02em; }
  .person__role { font-size: 13px; }
  .person__email { color: var(--ink-soft); }
  .services {
    position: absolute; left: 0; right: 0; top: 176px; height: 34px;
    background: var(--card-strip);
    font-size: 9px; letter-spacing: 0.04em; line-height: 1.35;
    text-align: center; padding-top: 4px; color: var(--ink-soft);
  }
  .services .sep { padding: 0 3px; }
  .web-band {
    position: absolute; left: 0; right: 0; bottom: 0; height: 42px;
    background: var(--card-band);
    font-family: "Open Sans", Arial, sans-serif; font-size: 11px;
    text-align: center; line-height: 42px; color: var(--ink-soft);
  }

  /* Brand panel */
  .brand-panel {
    position: absolute; left: 837px; top: 660px;
    width: 236px; height: 99px;
    background: var(--card);
    display: flex; align-items: center; justify-content: center; gap: 12px;
  }
  .brand-panel__dot { width: 34px; height: 34px; border-radius: 50%; background: var(--ink); }
  .brand-panel__name { font-size: 30px; letter-spacing: 0.05em; color: var(--ink); }
</style>
</head>
<body>
<main class="sheet">

  <section class="card card--back" aria-label="Business card, back">
    <div class="back-mark" aria-hidden="true"></div>
    <div class="offices">
      <div class="office">
        <p class="office__title">MAIN OFFICE:</p>
        <p>Kornblumenweg 14</p>
        <p>08352 Lindenfeld</p>
        <p>Germany</p>
      </div>
      <div class="office">
        <p class="office__title">BRANCH OFFICE:</p>
        <p>Daska Lane, Zarinkot</p>
        <p>Pakistan</p>
      </div>
    </div>
  </section>

  <section class="card card--front" aria-label="Business card, front">
    <div class="brand">
      <span class="brand__dot" aria-hidden="true"></span>
      <span class="brand__name">VORTANI</span>
    </div>
    <div class="person">
      <p class="person__name">LUKAS FELDHAUS <span class="person__role">(Owner)</span></p>
      <p class="person__email">lukas@vortani-example.com</p>
    </div>
    <div class="services">
      <p>PRIVATE LABELING<span class="sep">|</span>HIGH QUALITY PRODUCTION<span class="sep">|</span>DIRECT DISTRIBUTION</p>
      <p>WAREHOUSING<span class="sep">|</span>TRADEMARK REGISTRATION<span class="sep">|</span>LEGAL SUPPORT</p>
    </div>
    <div class="web-band">www.vortani-example.com</div>
  </section>

  <div class="brand-panel">
    <span class="brand-panel__dot" aria-hidden="true"></span>
    <span class="brand-panel__name">VORTANI</span>
  </div>

</main>
</body>
</html>
```